Business Card for Corinne Waldo

Name: Corinne Waldo
Title: Realtor
Email: Corinne@CorinneWaldoRE.example
Phone: 555-318-7492

On the front of the business card, I would like the photo, the contact information and the Corinne Waldo Logo. The backside is required to have the Broker logo and the required logos. Please use the colors from the logo design. Our company has a classy, professional look.

```html
<!DOCTYPE html>
<html lang="en">
<head>
<meta charset="utf-8">
<title>Corinne Waldo Real Estate – Business Card</title>
<link rel="stylesheet" href="https://fonts.googleapis.com/css2?family=Cinzel:wght@400;600&family=Arimo:wght@400;700&display=swap">
<style>
  :root {
    --backdrop: #e4e3e1;
    --card: #29292b;
    --card-edge: #202022;
    --brand-red: #a8182b;
    --ink-light: #f1f1f1;
    --ink-muted: #6f6f72;
    --photo-dark: #3a3a3c;
    --photo-light: #a9a9a9;
    --serif: "Cinzel", "Times New Roman", serif;
    --sans: "Arimo", Arial, sans-serif;
  }
  * { box-sizing: border-box; margin: 0; padding: 0; }
  html, body { width: 1200px; height: 801px; overflow: hidden; }
  body {
    background: var(--backdrop);
    display: flex;
    align-items: center;
    justify-content: center;
    gap: 44px;
    font-family: var(--sans);
  }
  .card {
    position: relative;
    width: 530px;
    height: 303px;
    background: var(--card);
    border: 1px solid var(--card-edge);
    overflow: hidden;
  }

  /* Front */
  .brand-lockup {
    position: absolute;
    display: flex;
    align-items: center;
    gap: 10px;
    color: var(--brand-red);
    font-family: var(--serif);
    font-weight: 600;
  }
  .card-front .brand-lockup { top: 42px; left: 210px; }
  .brand-mark {
    width: 26px; height: 26px;
    border: 2px solid currentColor;
  }
  .brand-name { font-size: 25px; line-height: 1; letter-spacing: 1px; }
  .brand-sub {
    display: block;
    font-size: 11px;
    letter-spacing: 2px;
    text-align: right;
    margin-top: 4px;
  }
  .brand-rule {
    position: absolute;
    top: 92px; left: 250px;
    width: 170px; height: 1px;
    background: var(--ink-light);
  }
  .agent-photo {
    position: absolute;
    left: 0; bottom: 0;
    width: 215px; height: 210px;
    background: linear-gradient(160deg, var(--photo-light) 0%, #6b6b6d 45%, var(--photo-dark) 100%);
  }
  .agent-id {
    position: absolute;
    right: 28px; top: 118px;
    text-align: right;
  }
  .agent-name {
    color: var(--brand-red);
    font-weight: 700;
    font-size: 23px;
  }
  .agent-title {
    color: var(--ink-muted);
    font-size: 17px;
    margin-top: 2px;
  }
  .contact-band {
    position: absolute;
    left: 215px; right: 0; top: 186px;
    height: 78px;
    background: var(--brand-red);
    color: var(--ink-light);
    padding: 12px 22px 0 20px;
    font-size: 16px;
    text-align: right;
  }
  .contact-line {
    display: flex;
    align-items: center;
    justify-content: flex-end;
    gap: 8px;
    line-height: 27px;
  }
  .contact-icon { width: 13px; height: 13px; flex: none; }

  /* Back */
  .card-back .brand-lockup {
    color: var(--ink-light);
    top: 72px; left: 50%;
    transform: translateX(-50%);
  }
  .card-back .brand-name { font-size: 30px; }
  .card-back .brand-mark { width: 32px; height: 32px; }
  .card-back .brand-rule { top: 130px; left: 170px; width: 190px; }
  .affiliations {
    position: absolute;
    left: 40px; right: 40px; bottom: 40px;
    display: flex;
    align-items: center;
    justify-content: space-between;
    color: var(--ink-light);
  }
  .broker {
    display: flex;
    align-items: center;
    gap: 8px;
    font-family: var(--serif);
    font-size: 15px;
  }
  .broker-mark {
    width: 18px; height: 18px;
    border: 1.5px solid currentColor;
    border-radius: 50%;
  }
  .badge-housing {
    width: 62px; height: 58px;
    border: 3px solid var(--ink-light);
  }
  .badge-listing {
    width: 150px; height: 58px;
    border: 3px solid var(--ink-light);
  }
</style>
</head>
<body>

  <section class="card card-front" aria-label="Business card front">
    <div class="brand-lockup">
      <span class="brand-mark"></span>
      <div>
        <span class="brand-name">Corinne Waldo</span>
        <span class="brand-sub">Real Estate</span>
      </div>
    </div>
    <div class="brand-rule"></div>

    <div class="agent-photo" role="img" aria-label="Black and white portrait photo of the realtor"></div>

    <div class="agent-id">
      <p class="agent-name">Corinne Waldo</p>
      <p class="agent-title">Realtor</p>
    </div>

    <div class="contact-band">
      <p class="contact-line">555-318-7492
        <svg class="contact-icon" viewBox="0 0 24 24" aria-hidden="true"><path fill="currentColor" d="M6.6 10.8a15 15 0 0 0 6.6 6.6l2.2-2.2a1 1 0 0 1 1-.25 11.4 11.4 0 0 0 3.6.6 1 1 0 0 1 1 1V20a1 1 0 0 1-1 1A17 17 0 0 1 3 4a1 1 0 0 1 1-1h3.5a1 1 0 0 1 1 1c0 1.25.2 2.45.6 3.6a1 1 0 0 1-.25 1z"/></svg>
      </p>
      <p class="contact-line">Corinne@CorinneWaldoRE.example
        <svg class="contact-icon" viewBox="0 0 24 24" aria-hidden="true"><rect x="2" y="5" width="20" height="14" fill="currentColor"/><path d="M2 5l10 8 10-8" fill="none" stroke="#a8182b" stroke-width="2"/></svg>
      </p>
    </div>
  </section>

  <section class="card card-back" aria-label="Business card back">
    <div class="brand-lockup">
      <span class="brand-mark"></span>
      <div>
        <span class="brand-name">Corinne Waldo</span>
        <span class="brand-sub">Real Estate</span>
      </div>
    </div>
    <div class="brand-rule"></div>

    <div class="affiliations">
      <div class="broker"><span class="broker-mark"></span>Halbrook Realty</div>
      <div class="badge-housing" role="img" aria-label="Fair housing badge"></div>
      <div class="badge-listing" role="img" aria-label="Realtor association and listing service badge"></div>
    </div>
  </section>

</body>
</html>
```